Bramblecrest Roofing Co. business card design

I am a Roofing contractor in Texas. The name of my company is Bramblecrest Roofing Co. I also offer a few other services (Christmas light installation, gutters, fencing, pressure washing). However my main gig is roofing. Storm restoration and knowledge of the insurance claim process is my specialty.

My colors are black, red and white. I’d like something pretty simple and clean. Modern looking but with a splash of this red tartan pattern.

I have another version of my logo being edited at the moment where the little top part of the F in roofing that’s currently tartan will be changed to just solid red to make it more visible. So if that’s something you can change in your mock up great. But I can provide the full version once the contest is complete

Target Market(s)

Homeowners

Industry/Entity Type

Roofing

Contact Information for Business Card

Darren Pike. 682-555-0193. www.bramblecrest roofing.example Darren@bramblecrestroofing.example

Colors
EB3D1F
EC4F4E
F09395
F8D3D4
FCEDEE

Requirements
Nice to have
• Maybe instead of a business address. I could say serving all DFW Texas or something like that. And maybe add a line somewhere saying deductible assistance? Just a thought

```html
<!DOCTYPE html>
<html lang="en">
<head>
<meta charset="utf-8">
<title>Bramblecrest Roofing Co. – Business Card</title>
<link href="https://fonts.googleapis.com/css2?family=Montserrat:wght@400;500;700;800&display=swap" rel="stylesheet">
<style>
  :root {
    --black: #050505;
    --red: #d81414;
    --red-deep: #b30f0f;
    --white: #ffffff;
    --paper: #fafafa;
    --backdrop: #3a3a3a;
    --grey-text: #e8e8e8;
  }
  * { margin: 0; padding: 0; box-sizing: border-box; }
  html, body {
    width: 1200px; height: 1200px; overflow: hidden;
    background: var(--backdrop);
    font-family: "Montserrat", sans-serif;
  }
  .sheet {
    width: 1200px; height: 1200px;
    display: flex; flex-direction: column; align-items: center; justify-content: center;
    gap: 60px;
  }
  .card {
    position: relative;
    width: 840px; height: 480px;
    border-radius: 34px;
    overflow: hidden;
    background: var(--black);
    box-shadow: 0 18px 40px rgba(0,0,0,.45);
  }

  /* Front */
  .card-front { background: var(--paper); }
  .front-shape { position: absolute; inset: 0; }
  .contact-block {
    position: absolute; left: 74px; top: 150px;
    color: var(--white);
  }
  .person {
    border-left: 6px solid var(--red);
    padding-left: 14px;
    margin-bottom: 26px;
  }
  .person-name {
    color: var(--red);
    font-size: 40px; font-weight: 500; letter-spacing: .5px;
    line-height: 1;
  }
  .person-role {
    font-size: 15px; font-weight: 400; letter-spacing: 1px; margin-top: 4px;
  }
  .contact-list { list-style: none; }
  .contact-list li {
    display: flex; align-items: center; gap: 14px;
    font-size: 21px; font-weight: 400; color: var(--grey-text);
    margin-bottom: 14px;
  }
  .contact-list svg { width: 24px; height: 24px; flex: none; }

  .brand-front {
    position: absolute; left: 590px; top: 90px; width: 230px;
    display: flex; flex-direction: column; align-items: center;
  }
  .brand-dot {
    border-radius: 50%; background: var(--red);
  }
  .brand-front .brand-dot { width: 110px; height: 110px; margin-bottom: 26px; }
  .brand-name {
    color: var(--red); font-weight: 800; text-transform: uppercase;
    text-align: center; line-height: 1.05;
  }
  .brand-front .brand-name { font-size: 29px; }

  /* Back */
  .brand-back {
    position: absolute; inset: 0;
    display: flex; flex-direction: column; align-items: center; justify-content: center;
  }
  .brand-back .brand-dot { width: 170px; height: 170px; margin-bottom: 34px; }
  .brand-back .brand-name { font-size: 54px; }
</style>
</head>
<body>
<main class="sheet">

  <section class="card card-front" aria-label="Business card front">
    <svg class="front-shape" viewBox="0 0 840 480" preserveAspectRatio="none" aria-hidden="true">
      <path d="M0 0 H352 C492 80 582 260 597 480 H0 Z" fill="var(--red)"/>
      <path d="M0 0 H330 C470 80 560 260 575 480 H0 Z" fill="var(--black)"/>
    </svg>

    <div class="contact-block">
      <div class="person">
        <div class="person-name">DARREN PIKE</div>
        <div class="person-role">OWNER</div>
      </div>
      <ul class="contact-list">
        <li>
          <svg viewBox="0 0 24 24" aria-hidden="true"><path fill="var(--red)" d="M6.6 10.8c1.4 2.8 3.8 5.1 6.6 6.6l2.2-2.2c.3-.3.7-.4 1-.2 1.1.4 2.3.6 3.6.6.6 0 1 .4 1 1V20c0 .6-.4 1-1 1C10.6 21 3 13.4 3 4c0-.6.4-1 1-1h3.5c.6 0 1 .4 1 1 0 1.3.2 2.5.6 3.6.1.3 0 .7-.2 1z"/></svg>
          682-555-0193
        </li>
        <li>
          <svg viewBox="0 0 24 24" aria-hidden="true"><rect x="2" y="5" width="20" height="14" rx="1" fill="var(--red)"/><path d="M2.5 5.5 12 13l9.5-7.5" stroke="var(--black)" stroke-width="1.6" fill="none"/></svg>
          darren@bramblecrestroofing.example
        </li>
        <li>
          <svg viewBox="0 0 24 24" aria-hidden="true"><g fill="none" stroke="var(--red)" stroke-width="2"><circle cx="12" cy="12" r="9.5"/><ellipse cx="12" cy="12" rx="4" ry="9.5"/><path d="M2.5 12h19M4 7h16M4 17h16"/></g></svg>
          www.bramblecrestroofing.example
        </li>
      </ul>
    </div>

    <div class="brand-front">
      <div class="brand-dot" aria-hidden="true"></div>
      <div class="brand-name">Bramblecrest<br>Roofing Co.</div>
    </div>
  </section>

  <section class="card card-back" aria-label="Business card back">
    <div class="brand-back">
      <div class="brand-dot" aria-hidden="true"></div>
      <div class="brand-name">Bramblecrest<br>Roofing Co.</div>
    </div>
  </section>

</main>
</body>
</html>
```